Waste Oil Filter collection & disposal

Basically I need a 1 page website for the business called Brenmoor Waste Solutions.
We are a environmental service provider and we collect and dispose of waste oil filters to protect the environment from hazardous waste oil products.

This is the link to our current website: www.brenmoorwaste.co.nz

we want it to look fresh and better than our current website. we may potentially look at getting a new logo designed and are open to ideas/designs if you have any.

Industry/Entity Type

Business

Logo Text

Brenmoor Waste Solutions

Number of Pages Required

1 page

Requirements
Must have
• same colours as current website.
• description of what service we provide please refer to leaflet attached

```html
<!DOCTYPE html>
<html lang="en">
<head>
<meta charset="utf-8">
<title>Brenmoor Waste Solutions Ltd</title>
<link href="https://fonts.googleapis.com/css2?family=Roboto:wght@300;400;500;700&display=swap" rel="stylesheet">
<style>
:root{
  --green:#3cb43c;
  --ink:#1a1a1a;
  --text:#333;
  --muted:#666;
  --light:#f1f1f1;
  --light-2:#e6e6e6;
  --white:#fff;
}
*{box-sizing:border-box;margin:0;padding:0}
html,body{width:1200px;height:4000px;overflow:hidden}
body{font-family:"Roboto",Arial,sans-serif;color:var(--text);background:var(--white);position:relative}
section,header,footer{position:absolute;left:0;width:1200px}

/* hero */
.hero{top:0;height:672px;background:radial-gradient(ellipse at 50% 55%,#4a4a4a 0%,#262626 45%,#0d0d0d 100%)}
.brand{position:absolute;left:107px;top:32px;display:flex;align-items:center;gap:20px}
.brand-mark{width:160px;height:75px;background:var(--white);display:flex;align-items:center;justify-content:center;gap:8px;padding:0 10px}
.brand-mark .dot{width:16px;height:16px;background:var(--green);flex:none}
.brand-mark span{font-size:12px;font-weight:700;color:var(--ink);line-height:1.15}
.brand-name{color:var(--white);font-weight:700;font-size:19px;border-bottom:2px solid var(--white);padding-bottom:6px}
.brand-tag{color:var(--white);font-size:12px;margin-top:6px;letter-spacing:.3px}
.top-contact{position:absolute;right:107px;top:44px;display:flex;gap:30px;color:var(--white);font-size:13px;align-items:center}
.top-contact span{display:flex;align-items:center;gap:8px}
.hero-title{position:absolute;left:219px;top:280px;width:765px;border-top:10px solid var(--green);border-bottom:10px solid var(--green);padding:12px 0;line-height:57px;text-align:center;color:var(--white);font-size:47px;font-weight:500;white-space:nowrap}
.hero-title em{font-style:normal;color:var(--green)}

/* intro */
.intro{top:672px;height:307px;background:var(--light)}
.intro-copy{position:absolute;left:107px;top:54px;width:700px}
.intro-copy h2{color:var(--green);font-size:25px;font-weight:500;margin-bottom:6px}
.intro-copy .lead{font-size:18px;color:var(--ink);line-height:1.4;padding-bottom:10px;border-bottom:4px solid #bbb;width:600px}
.intro-copy p{font-size:14px;color:var(--muted);line-height:1.6;margin-top:14px;width:690px}
.intro-art{position:absolute;left:810px;top:50px;width:210px;height:210px;border-radius:50%;background:radial-gradient(circle,#6d6d6d,#1f1f1f)}

/* statement */
.statement{top:979px;height:234px;background:linear-gradient(180deg,#3fbf3f,#2ea52e);display:flex;align-items:center;justify-content:center}
.statement h2{width:1000px;text-align:center;font-size:31px;font-weight:500;color:var(--ink);line-height:1.35}

/* features */
.features{top:1213px;height:374px;display:flex}
.feature{flex:1;text-align:center;padding:44px 36px 0}
.feature:nth-child(odd){background:var(--light-2)}
.feature:nth-child(even){background:var(--light)}
.feature .badge{width:100px;height:100px;border-radius:50%;background:var(--green);margin:0 auto 44px;display:flex;align-items:center;justify-content:center}
.feature p{font-size:16px;font-weight:500;color:var(--ink);line-height:1.75;text-transform:uppercase}

/* quotes */
.quotes{top:1587px;height:706px;background:radial-gradient(ellipse at 50% 40%,#3d3d3d,#101010);border-top:5px solid var(--green);border-bottom:5px solid var(--green)}
.quote{position:absolute;top:168px;height:360px;background:var(--white);padding:70px 28px 0}
.quote.alt{background:var(--green)}
.quote .bubble{position:absolute;left:22px;top:-36px;width:76px;height:76px;border-radius:50%;background:var(--green);border:5px solid var(--white);display:flex;align-items:center;justify-content:center}
.quote.alt .bubble{background:var(--ink)}
.quote p{font-size:21px;line-height:1.35;color:var(--ink)}
.quote.alt p{color:var(--white)}
.quote .source{position:absolute;right:24px;bottom:40px;background:var(--green);color:var(--white);font-size:15px;border-radius:14px;padding:5px 26px;white-space:nowrap}
.quote.alt .source{background:var(--ink)}

/* gallery */
.gallery{top:2293px;height:710px;background:var(--white);border-bottom:8px solid var(--green)}
.pill{display:inline-block;background:var(--ink);color:var(--white);border-radius:30px;font-size:30px;font-weight:500}
.gallery .pill{position:absolute;left:427px;top:57px;width:400px;text-align:center;padding:4px 0}
.tile{position:absolute;width:312px;height:220px;border:3px solid #ddd}
.tile.t1{background:linear-gradient(135deg,#3a3a3a,#1a1a1a)}
.tile.t2{background:linear-gradient(135deg,#6f8f7c,#2c5f49)}
.tile.t3{background:linear-gradient(135deg,#8b8d90,#3c3e42)}
.tile.t4{background:linear-gradient(135deg,#5a7468,#2f4a3d)}
.tile.t5{background:linear-gradient(135deg,#4d4f57,#1b1c22)}
.tile.t6{background:linear-gradient(135deg,#6b6e78,#2e3036)}
.tile-caption{position:absolute;inset:0;text-align:center;color:var(--white);padding-top:46px}
.tile-caption h3{font-size:17px;font-weight:500;display:inline-block;padding:0 28px 6px;border-bottom:1px solid #999}
.tile-caption p{font-size:14px;margin:14px 0 12px}
.tile-caption .more{display:inline-block;background:var(--green);border-radius:12px;font-size:13px;padding:3px 20px}
.tile-share{position:absolute;right:12px;bottom:12px;width:30px;height:30px;border-radius:50%;background:var(--green)}

/* process */
.process{top:3003px;height:645px;background:var(--white)}
.process .pill{position:absolute;left:107px;top:72px;width:253px;padding:3px 0 3px 40px;font-size:28px}
.process-copy{position:absolute;left:112px;top:128px;width:600px;font-size:16px;line-height:1.75;color:var(--ink)}
.steps{list-style:none;margin:14px 0 0 30px}
.steps li{position:relative;display:flex;align-items:center;gap:22px;height:43px;font-size:15px;color:var(--muted)}
.steps li::before{content:"";width:26px;height:26px;border-radius:50%;background:var(--green);flex:none}
.steps li svg{position:absolute;left:7px}
.process-copy h3{font-size:20px;font-weight:500;color:#444;border-bottom:3px solid #ccc;width:440px;padding-bottom:4px;margin:18px 0 10px -10px}
.process-art{position:absolute;left:715px;top:130px;width:373px;height:294px;background:linear-gradient(135deg,#7a9084,#344a3f);box-shadow:6px 8px 14px rgba(0,0,0,.3)}

/* contact */
.contact{top:3648px;height:312px;background:radial-gradient(ellipse at 50% 40%,#3a3a3a,#0e0e0e)}
.contact h2{position:absolute;left:0;width:1200px;top:44px;text-align:center;color:var(--white);font-size:30px;font-weight:500}
.contact h2::after{content:"";display:block;width:480px;height:2px;background:#bbb;margin:10px auto 0}
.contact-list{position:absolute;left:287px;top:117px;list-style:none;color:var(--white);font-size:15px}
.contact-list li{display:flex;align-items:center;gap:14px;height:44px}
.contact-list .ico{width:28px;height:28px;border-radius:50%;background:var(--green);display:flex;align-items:center;justify-content:center}
.pricing{position:absolute;left:691px;top:117px;list-style:none;color:var(--white);font-size:17px}
.pricing li{height:44px;display:flex;align-items:center}
.pricing b{font-weight:400;color:var(--green);margin-left:6px}
.site-foot{top:3960px;height:40px;background:var(--ink);color:var(--white);font-size:13px;display:flex;align-items:center;padding-left:96px}
</style>
</head>
<body>

<header class="hero" role="img" aria-label="Dark photo of a used oil filter">
  <div class="brand">
    <div class="brand-mark"><span class="dot"></span><span>BRENMOOR WASTE SOLUTIONS</span></div>
    <div>
      <div class="brand-name">BRENMOOR WASTE SOLUTIONS LTD</div>
      <div class="brand-tag">OIL FILTER COLLECTION &amp; DISPOSAL SERVICE</div>
    </div>
  </div>
  <div class="top-contact">
    <span><svg width="16" height="12" viewBox="0 0 16 12"><rect width="16" height="12" rx="1" fill="#3cb43c"/><path d="M1 1l7 6 7-6" stroke="#fff" fill="none" stroke-width="1.5"/></svg>info@brenmoorwaste.co.nz</span>
    <span><svg width="14" height="14" viewBox="0 0 24 24"><path fill="#3cb43c" d="M6.6 10.8a15 15 0 006.6 6.6l2.2-2.2c.3-.3.7-.4 1-.2 1.1.4 2.3.6 3.6.6.6 0 1 .4 1 1V20c0 .6-.4 1-1 1A17 17 0 013 4c0-.6.4-1 1-1h3.5c.6 0 1 .4 1 1 0 1.3.2 2.5.6 3.6.1.3 0 .7-.2 1z"/></svg>06 555 0142</span>
  </div>
  <h1 class="hero-title">KEEPING <em>NEW ZEALAND</em> GREEN</h1>
</header>

<section class="intro">
  <div class="intro-copy">
    <h2>BRENMOOR WASTE SOLUTIONS LTD</h2>
    <div class="lead">Specialize in the collection &amp; disposal of oil / fuel filters, servicing the lower north island on a monthly cycle.</div>
    <p>We offer a cost effective environmentally friendly system for the collection and disposal of waste oil filters helping minimise contamination of landfills keeping your industry compliant.</p>
  </div>
  <div class="intro-art" role="img" aria-label="Illustration of an oil filter"></div>
</section>

<section class="statement">
  <h2>BRENMOOR WASTE SOLUTIONS LTD SERVICE THE LOWER NORTH ISLAND AND SPECIALISE IN THE COLLECTION &amp; DISPOSAL OF OIL &amp; FUEL FILTERS</h2>
</section>

<section class="features">
  <div class="feature">
    <div class="badge"><svg width="50" height="50" viewBox="0 0 24 24"><path fill="#fff" d="M12 3c4 2 6 5 5 9-1 3-4 4-5 4 0-3 1-6 3-8-3 2-4 5-4 8-2-1-4-3-4-6 0-4 3-6 5-7zM3 18h7l3 1 5-2c1 0 1 1 0 2l-6 3H3z"/></svg></div>
    <p>We are passionate about doing our bit in keeping New Zealand clean and green.</p>
  </div>
  <div class="feature">
    <div class="badge"><svg width="50" height="50" viewBox="0 0 24 24"><path fill="#fff" d="M12 3l10 9h-3v9h-5v-6h-4v6H5v-9H2z"/></svg></div>
    <p>Our processes are environmentally friendly and minimise the contamination of landfills.</p>
  </div>
  <div class="feature">
    <div class="badge"><svg width="44" height="54" viewBox="0 0 20 24"><rect x="3" y="1" width="14" height="3" rx="1" fill="#fff"/><rect x="4" y="5" width="12" height="18" rx="1" fill="#fff"/><path d="M7 7v14M10 7v14M13 7v14" stroke="#3cb43c" stroke-width="1.2"/></svg></div>
    <p>We offer a cost effective system for the collection and disposal of waste oil filters.</p>
  </div>
  <div class="feature">
    <div class="badge"><svg width="50" height="50" viewBox="0 0 24 24"><circle cx="12" cy="12" r="10" fill="none" stroke="#fff" stroke-width="2.4"/><rect x="10.8" y="6" width="2.4" height="8" fill="#fff"/><circle cx="12" cy="17.3" r="1.5" fill="#fff"/></svg></div>
    <p>We keep your industry compliant.</p>
  </div>
</section>

<section class="quotes" role="group" aria-label="Oil recycling facts">
  <div class="quote" style="left:133px;width:286px">
    <div class="bubble"><svg width="32" height="28" viewBox="0 0 24 20"><path fill="#fff" d="M3 2h18v12H9l-5 4v-4H3z"/></svg></div>
    <p>"Each used oil filter has on aver age, more than quarter of a litre of used motor oil "</p>
    <span class="source">Green Loop Trust</span>
  </div>
  <div class="quote alt" style="left:443px;width:312px">
    <div class="bubble"><svg width="32" height="28" viewBox="0 0 24 20"><path fill="#fff" d="M3 2h18v12H9l-5 4v-4H3z"/></svg></div>
    <p>"Recycling engine oil protects the environment and conserves energy resources."</p>
    <span class="source">Oil Recycling</span>
  </div>
  <div class="quote" style="left:781px;width:307px">
    <div class="bubble"><svg width="32" height="28" viewBox="0 0 24 20"><path fill="#fff" d="M3 2h18v12H9l-5 4v-4H3z"/></svg></div>
    <p>"One litre of used oil can contaminate one million litres of water "</p>
    <span class="source">Harbourview District Council</span>
  </div>
</section>

<section class="gallery">
  <h2 class="pill">MY GALLERY</h2>
  <div class="tile t1" style="left:107px;top:163px" role="img" aria-label="Collection truck">
    <div class="tile-caption"><h3>VEHICLES</h3><p>Purpose built truck for collection</p><span class="more">Read More</span></div>
    <span class="tile-share"></span>
  </div>
  <div class="tile t2" style="left:443px;top:163px" role="img" aria-label="Filter crushing machine"></div>
  <div class="tile t3" style="left:776px;top:163px" role="img" aria-label="Processing plant floor"></div>
  <div class="tile t4" style="left:107px;top:411px" role="img" aria-label="Sorting conveyor with filters"></div>
  <div class="tile t5" style="left:443px;top:411px" role="img" aria-label="Pile of used oil filters"></div>
  <div class="tile t6" style="left:776px;top:411px" role="img" aria-label="Stacked filter bricks ready for recycling"></div>
</section>

<section class="process">
  <h2 class="pill">THE PROCESS</h2>
  <div class="process-copy">
    <p>Filters are collected and transported back to the processing plant.<br>At the processing plant they are:</p>
    <ul class="steps">
      <li><svg width="12" height="12" viewBox="0 0 12 12"><path d="M3 2l5 4-5 4" stroke="#fff" stroke-width="2" fill="none"/></svg>Drained</li>
      <li><svg width="12" height="12" viewBox="0 0 12 12"><path d="M3 2l5 4-5 4" stroke="#fff" stroke-width="2" fill="none"/></svg>Sorted</li>
      <li><svg width="12" height="12" viewBox="0 0 12 12"><path d="M3 2l5 4-5 4" stroke="#fff" stroke-width="2" fill="none"/></svg>Drained again</li>
      <li><svg width="12" height="12" viewBox="0 0 12 12"><path d="M3 2l5 4-5 4" stroke="#fff" stroke-width="2" fill="none"/></svg>Crushed into bricks</li>
      <li><svg width="12" height="12" viewBox="0 0 12 12"><path d="M3 2l5 4-5 4" stroke="#fff" stroke-width="2" fill="none"/></svg>Drained a third time</li>
      <li><svg width="12" height="12" viewBox="0 0 12 12"><path d="M3 2l5 4-5 4" stroke="#fff" stroke-width="2" fill="none"/></svg>Stacked ready for Metal Recycling</li>
    </ul>
    <h3>WHAT HAPPENS TO THE OIL</h3>
    <p>All residual oil is collected into our tank and then recycled.<br>Currently we are processing over 2,000 litres of oil amonth.</p>
  </div>
  <div class="process-art" role="img" aria-label="Filters on the processing line"></div>
</section>

<section class="contact">
  <h2>READY TO HELP YOU</h2>
  <ul class="contact-list">
    <li><span class="ico"><svg width="14" height="14" viewBox="0 0 24 24"><circle cx="12" cy="12" r="9" fill="none" stroke="#fff" stroke-width="2"/><path d="M3 12h18M12 3c3 3 3 15 0 18M12 3c-3 3-3 15 0 18" stroke="#fff" stroke-width="1.6" fill="none"/></svg></span>www.brenmoorwaste.co.nz</li>
    <li><span class="ico"><svg width="14" height="11" viewBox="0 0 16 12"><rect width="16" height="12" rx="1" fill="#fff"/><path d="M1 1l7 6 7-6" stroke="#3cb43c" fill="none" stroke-width="1.5"/></svg></span>info@brenmoorwaste.co.nz</li>
    <li><span class="ico"><svg width="13" height="13" viewBox="0 0 24 24"><path fill="#fff" d="M6.6 10.8a15 15 0 006.6 6.6l2.2-2.2c.3-.3.7-.4 1-.2 1.1.4 2.3.6 3.6.6.6 0 1 .4 1 1V20c0 .6-.4 1-1 1A17 17 0 013 4c0-.6.4-1 1-1h3.5c.6 0 1 .4 1 1 0 1.3.2 2.5.6 3.6.1.3 0 .7-.2 1z"/></svg></span>06 555 0142</li>
  </ul>
  <ul class="pricing">
    <li>Monthly Bin Collection: <b>$65.00</b></li>
    <li>Addit ional Bins: <b>$35.00 ea</b></li>
    <li>Account Set Up Fee: <b>$85.00</b></li>
  </ul>
</section>

<footer class="site-foot">Brenmoor Waste Solutions Ltd</footer>

</body>
</html>
```